" Nome da empresa: Recanto Vivale CLINICA DE NUTRIÇAO SOMOS NUTRICIONISTAS E DESEJAMOS PROPORCIONAR AOS NOSSOS PACIENTES UM TRATAMENTO INDIVIDUALIZADO. FAREMOS ATENDIMENTOS NUTRICIONAIS A FIM DE LEVAR QUALIDADE DE VIDA E PREVENÇAO de doenças, focando na educaçao nutricional "

```html
<!DOCTYPE html>
<html lang="pt-BR">
<head>
<meta charset="utf-8">
<title>Recanto Vivale — Cartão de visita</title>
<link href="https://fonts.googleapis.com/css2?family=Questrial&display=swap" rel="stylesheet">
<style>
  :root {
    --teal: #1f6b62;
    --teal-dark: #1a4f4a;
    --orange: #e0922f;
    --card: #ffffff;
    --backdrop: #ecebe7;
    --muted: #5f6f6c;
  }
  html, body {
    margin: 0;
    padding: 0;
    width: 1200px;
    height: 1200px;
    overflow: hidden;
    background: var(--backdrop);
    font-family: "Questrial", Arial, sans-serif;
  }
  .canvas {
    position: relative;
    width: 1200px;
    height: 1200px;
  }
  .business-card {
    position: absolute;
    left: 140px;
    top: 474px;
    width: 918px;
    height: 252px;
    background: var(--card);
    box-shadow: 0 2px 10px rgba(0,0,0,0.12);
  }
  .brand {
    position: absolute;
    left: 36px;
    top: 40px;
    width: 250px;
  }
  .brand-dot {
    display: block;
    width: 46px;
    height: 46px;
    border-radius: 50%;
    background: var(--orange);
    margin: 0 0 20px 58px;
  }
  .brand-name {
    margin: 0;
    font-size: 34px;
    font-weight: 400;
    color: var(--teal);
    letter-spacing: 0.5px;
    white-space: nowrap;
  }
  .brand-tagline {
    margin: 8px 0 0;
    font-size: 9px;
    color: var(--muted);
    letter-spacing: 0.3px;
    white-space: nowrap;
  }
  .divider {
    position: absolute;
    left: 322px;
    top: 41px;
    width: 7px;
    height: 144px;
  }
  .contact {
    position: absolute;
    left: 379px;
    top: 44px;
    color: var(--teal-dark);
  }
  .contact-name {
    margin: 0;
    font-size: 19px;
    font-weight: 400;
    color: var(--teal-dark);
  }
  .contact-role {
    margin: 2px 0 0;
    font-size: 9px;
    color: var(--muted);
  }
  .contact-details {
    margin: 24px 0 0;
    font-size: 11px;
    line-height: 15px;
    font-style: normal;
  }
  .contact-details p { margin: 0; }
  .contact-address { margin-top: 5px !important; }
</style>
</head>
<body>
<main class="canvas">
  <article class="business-card">
    <section class="brand">
      <span class="brand-dot" aria-hidden="true"></span>
      <h1 class="brand-name">Recanto Vivale</h1>
      <p class="brand-tagline">Saúde · Clínica · Educação Nutricional</p>
    </section>

    <svg class="divider" viewBox="0 0 7 144" aria-hidden="true">
      <rect x="0" y="0" width="7" height="64" fill="var(--orange)"/>
      <rect x="0" y="70" width="7" height="74" fill="var(--teal)"/>
    </svg>

    <section class="contact">
      <h2 class="contact-name">Nome Sobrenome</h2>
      <p class="contact-role">Função</p>
      <address class="contact-details">
        <p>Tel 0000-0000</p>
        <p>Cel 0000.0000</p>
        <p>Email contato@recantovivale.com.br</p>
        <p class="contact-address">Endereço Rua das Flores,00 Bairro</p>
        <p>Jardins, Cidade das Flores</p>
      </address>
    </section>
  </article>
</main>
</body>
</html>
```